Advertising company unique advertising platform

we need a logo design for a new company based in Australia Melbourne. We develop innovated advertising platform where consumer can use this platform to get regular discount, as business owner they can use this platform for free advertisement. Payment for this advertisement platform only payable every two weeks, when I generate revenue for their business

Industry/Entity Type

Advertising

Contact Information for Business Card

Dale Pruitt | Co-Founder |Managing Director
Suite 718 263 Harrowgate Row Melbourne Vic 3000

ABN 41 902 615 273
Tel: +61 0491 528 307 | Email: dale.pruitt@corvelaxtro.com

Font styles to use
Decorative
Script

Requirements
Must have
• Try few different design and some round corner business card
Should not have
• One round corner business card...try 4 different colour background not only black, make sure two side is designed. Be creative so imagine you are giving this to a client make sure has wow factor, if you can also try one design with engrave like all the logo, words look 3d feel
• The word Advertising Platform use attached file font

```html
<!DOCTYPE html>
<html lang="en">
<head>
<meta charset="utf-8">
<title>Corvelax Hub – Business Card</title>
<link href="https://fonts.googleapis.com/css2?family=Source+Sans+3:wght@300;400;600;700&display=swap" rel="stylesheet">
<style>
  :root {
    --backdrop: #c9d0d8;
    --card: #2a2a2b;
    --card-edge: #333335;
    --text-strong: #f1f1f1;
    --text-soft: #d6d6d6;
    --accent-orange: #e4703a;
    --accent-teal: #2fd3ae;
  }
  * { margin: 0; padding: 0; box-sizing: border-box; }
  html, body {
    width: 1200px; height: 675px; overflow: hidden;
    background: var(--backdrop);
    font-family: "Source Sans 3", "Myriad Pro", sans-serif;
  }
  .stage {
    width: 1200px; height: 675px;
    display: flex; align-items: center; justify-content: center;
  }
  .business-card {
    position: relative;
    width: 880px; height: 500px;
    background: linear-gradient(160deg, var(--card-edge), var(--card));
    box-shadow: 0 18px 40px rgba(0,0,0,0.25);
  }
  .contact-block {
    position: absolute; left: 70px; top: 70px;
    color: var(--text-soft);
  }
  .person-name {
    font-size: 30px; font-weight: 700; color: var(--text-strong);
    line-height: 1.1;
  }
  .person-role {
    font-size: 19px; font-weight: 300; line-height: 1.3;
    margin-top: 4px;
  }
  .contact-list { list-style: none; margin-top: 38px; }
  .contact-item {
    display: flex; align-items: flex-start; gap: 14px;
    font-size: 19px; font-weight: 400; line-height: 1.32;
    margin-bottom: 16px;
  }
  .contact-icon { width: 18px; height: 18px; flex: none; margin-top: 4px; }
  .brand-block {
    position: absolute; left: 470px; top: 190px; width: 360px;
    text-align: center;
  }
  .brand-mark {
    display: flex; align-items: center; justify-content: center; gap: 16px;
  }
  .brand-dot {
    width: 26px; height: 26px; border-radius: 50%;
    background: var(--accent-orange);
  }
  .brand-name {
    font-size: 52px; font-weight: 700; color: var(--accent-teal);
    line-height: 1; letter-spacing: 0.5px;
  }
  .business-number {
    margin-top: 60px;
    font-size: 22px; font-weight: 400; color: var(--text-strong);
    letter-spacing: 0.5px;
  }
</style>
</head>
<body>
<main class="stage">
  <section class="business-card" aria-label="Business card front">
    <div class="contact-block">
      <h1 class="person-name">Dale Pruitt</h1>
      <p class="person-role">Co-Founder | Managing Director<br>Founder &amp; Director</p>
      <ul class="contact-list">
        <li class="contact-item">
          <svg class="contact-icon" viewBox="0 0 24 24" aria-hidden="true"><path fill="var(--accent-orange)" d="M12 2a7 7 0 0 0-7 7c0 5 7 13 7 13s7-8 7-13a7 7 0 0 0-7-7zm0 9.5A2.5 2.5 0 1 1 12 6.5a2.5 2.5 0 0 1 0 5z"/></svg>
          <span>Suite 718 263<br>Harrowgate Row<br>Melbourne Vic 3000</span>
        </li>
        <li class="contact-item">
          <svg class="contact-icon" viewBox="0 0 24 24" aria-hidden="true"><path fill="var(--accent-orange)" d="M6.6 10.8a15 15 0 0 0 6.6 6.6l2.2-2.2a1 1 0 0 1 1-.25 11.4 11.4 0 0 0 3.6.57 1 1 0 0 1 1 1V20a1 1 0 0 1-1 1A17 17 0 0 1 3 4a1 1 0 0 1 1-1h3.5a1 1 0 0 1 1 1c0 1.25.2 2.45.57 3.57a1 1 0 0 1-.25 1z"/></svg>
          <span>+61 0491 528 307</span>
        </li>
        <li class="contact-item">
          <svg class="contact-icon" viewBox="0 0 24 24" aria-hidden="true"><rect x="2" y="5" width="20" height="14" rx="1" fill="var(--accent-orange)"/><path d="M2.5 6l9.5 7 9.5-7" fill="none" stroke="var(--card)" stroke-width="1.6"/></svg>
          <span>dale.pruitt@corvelaxtro.com</span>
        </li>
        <li class="contact-item">
          <svg class="contact-icon" viewBox="0 0 24 24" aria-hidden="true"><circle cx="12" cy="12" r="10" fill="var(--accent-orange)"/><path d="M2 12h20M12 2c3 3 3 17 0 20M12 2c-3 3-3 17 0 20" fill="none" stroke="var(--card)" stroke-width="1.4"/></svg>
          <span>www.corvelaxtro.com</span>
        </li>
      </ul>
    </div>
    <div class="brand-block">
      <div class="brand-mark">
        <span class="brand-dot" aria-hidden="true"></span>
        <span class="brand-name">Corvelax Hub</span>
      </div>
      <p class="business-number">ABN 41 902 615 273</p>
    </div>
  </section>
</main>
</body>
</html>
```